WP website design (Brannock)

We need a wordpress design that will incorporate a professional color scheme with company logo in a clean layout. The design needs to consider that this will be developed on a responsive theme. Colors are that of the logo and and an accent color (perhaps light brown/tan). Client wants a 'modern' look.

Industry/Entity Type

It Company

Font styles to use
Serif
Sans Serif

Colors

Designer to choose colors to be used in the design.

Requirements
Must have
• Must Have:
- Navigation: 1) Home 2) Real Estate Listings 3) Auctions 4) Buyers 5) Sellers 6) Services 7) Meet the Crew 8) Contact Us

Site will have a slideshow element (image attached) and the following widgets: 1) Featured Auctions 2) Testimonials blog widget 3) 'Auction Alerts' email sign up 4) FB Twitter RSS.

In the footer, there will be smaller company logo, the affiliations logo, and contact info below:
Brannock Auctions & Realty, Inc.
30915 Quill Meadow Road • Suite 508 • Orlando, FL 32828
Office: 407.555.0142 / Cell: 407.555.0187 / Fax: 407.555.0163
Email: info@brannockauctions.example
Nice to have
• - - Site will have drop-down menus - please indicate the styling, for instance the dropdown menus 1) Upcoming Auctions 2) Past Auctions under the 'Auctions' link

```html
<!DOCTYPE html>
<html lang="en">
<head>
<meta charset="utf-8">
<title>Brannock Auctions &amp; Realty</title>
<link rel="stylesheet" href="https://fonts.googleapis.com/css2?family=Cinzel:wght@400;500&family=Libre+Baskerville&family=Roboto:ital,wght@0,400;0,500;0,700;1,400&family=Source+Sans+3:wght@400;600&display=swap">
<style>
:root{
  --page:#f0c9aa;
  --red:#a3222d;
  --red-dark:#8a1a24;
  --ink:#222;
  --card:#fdf0e6;
  --line:#d9b79b;
  --black:#111;
  --white:#fff;
  --link:#d6142d;
}
*{box-sizing:border-box;margin:0;padding:0}
html,body{width:1131px;height:1200px;overflow:hidden}
body{background:var(--page);position:relative;font-family:"Roboto",Arial,sans-serif;color:var(--ink)}
.abs{position:absolute}

.brand{left:97px;top:18px;color:var(--red);font-family:"Libre Baskerville",serif;text-align:center;line-height:1}
.brand .name{font-size:50px;letter-spacing:-1px}
.brand .sub{font-size:18px;letter-spacing:10px;margin-top:6px}

.social{left:675px;top:40px;display:flex;align-items:center;gap:20px}
.social-label{font-family:"Source Sans 3",sans-serif;font-size:21px;color:#333;margin-right:12px}
.social-tile{width:45px;height:45px;border-radius:3px}
.tile-a{background:#3b5b9c}
.tile-b{background:#33b5e8}
.tile-c{background:#e8702f}

.nav{left:0;top:122px;width:1131px;height:47px;background:linear-gradient(#b12733,var(--red-dark))}
.nav ul{list-style:none;display:flex;position:absolute;left:105px;top:0;height:47px}
.nav li{font-family:"Source Sans 3",sans-serif;font-weight:600;font-size:15px;color:var(--white);padding:0 23px;line-height:47px;position:relative}
.nav li+li::before{content:"";position:absolute;left:0;top:11px;height:26px;border-left:1px solid #c95860}
.nav li.active{background:var(--black);padding:0 13px}
.nav li.active+li::before{display:none}

.dropdown{left:375px;top:169px;width:161px;background:var(--red);border-bottom:3px solid var(--red);font-family:"Source Sans 3",sans-serif;font-size:15px;color:var(--white);z-index:5}
.dropdown div{height:34px;line-height:34px;padding-left:15px}
.dropdown .hover{background:#1a1a1a}

.slider{left:102px;top:177px;width:645px;height:272px;border:2px solid var(--white);background:linear-gradient(180deg,#6aa2d8 0%,#b9c3c6 40%,#8c9289 70%,#4f6a3e 100%)}
.slider .share{position:absolute;right:14px;top:14px;width:26px;height:26px}
.dots{position:absolute;left:292px;bottom:10px;display:flex;gap:11px}
.dots span{width:17px;height:17px;border-radius:50%;background:var(--red);border:1px solid #6e141b}
.dots span.on{background:var(--white);border-color:#ddd}

.alert{left:757px;top:177px;width:272px;height:272px;background:linear-gradient(#2b2b2b,#000);color:var(--white);padding:28px 17px}
.alert h2{font-family:"Cinzel",serif;font-weight:400;font-size:27px;line-height:1}
.alert p{font-family:"Source Sans 3",sans-serif;font-size:14px;line-height:19px;margin-top:14px}
.alert .field{width:231px;height:33px;background:var(--white);margin-top:21px;font-size:13px;color:#777;line-height:33px;padding-left:11px}
.alert .btn{width:105px;height:33px;background:var(--red);margin-top:27px;font-family:"Source Sans 3",sans-serif;font-weight:600;font-size:18px;line-height:33px;text-align:center}

.tagline{left:95px;top:484px;width:642px;text-align:center;font-family:"Source Sans 3",sans-serif;font-size:21px;line-height:32px;color:#1c1c1c}

.listing{left:135px;top:591px;width:577px;height:292px;background:var(--card);border:1px solid var(--line);border-radius:7px 7px 0 0}
.listing-head{height:42px;background:linear-gradient(#3a3a3a,#000);border-radius:6px 6px 0 0;color:var(--white);font-weight:500;font-size:17px;letter-spacing:.5px;line-height:44px;padding-left:20px}
.thumb{position:absolute;left:32px;top:53px;width:150px;height:100px;background:linear-gradient(#7aa6cf,#b2b9b9 45%,#567146);box-shadow:2px 2px 3px rgba(0,0,0,.35)}
.action{position:absolute;left:66px;width:99px;height:33px;background:var(--red);border:1px solid #d9707a;border-radius:4px;color:var(--white);font-size:13px;line-height:31px;padding-left:38px}
.action svg{position:absolute;left:11px;top:7px}
.listing-body{position:absolute;left:209px;top:64px;font-size:13px;line-height:18px;letter-spacing:.3px}
.listing-body h3{font-family:"Source Sans 3",sans-serif;font-weight:600;font-size:16px;letter-spacing:1px}
.listing-body .desc{margin-top:9px;width:310px}
.sale-link{color:var(--link);font-weight:700;font-size:14px;margin:9px 0 0 100px}
.listing-body .strong{font-weight:500;margin-top:12px}
.pin{display:inline-block;vertical-align:-2px;margin-right:4px}
.when{margin-left:61px}

.partner{left:348px;top:911px;width:179px;height:58px;background:var(--white);border:1px solid #ccc;border-radius:6px}
.partner span{position:absolute;left:12px;top:14px;width:150px;height:26px;background:#dfe3ea;border-radius:13px}

.widget{left:755px;width:273px;background:var(--card);border:1px solid var(--line)}
.widget-head{height:47px;background:var(--red);color:var(--white);font-family:"Source Sans 3",sans-serif;font-size:27px;line-height:49px;padding-left:22px;border-radius:4px 4px 0 0;margin:-1px -1px 0}
.featured{top:477px;height:294px;text-align:center;font-size:12px;line-height:16px}
.featured .title{font-weight:500;margin-top:16px}
.featured .img{width:169px;height:102px;margin:12px auto 0;border:2px solid #333;background:linear-gradient(#7aa6cf,#b2b9b9 45%,#567146)}
.featured .lots{margin-top:22px}
.testimonials{top:803px;height:228px}
.testimonials blockquote{font-style:italic;font-size:13px;line-height:19px;padding:18px 12px 0 22px;position:relative;text-indent:26px}
.testimonials blockquote svg{position:absolute;left:16px;top:16px}
.testimonials .author{font-style:italic;font-size:13px;color:var(--red);padding:9px 0 0 20px}

.footer{left:0;top:1073px;width:1131px;height:127px;background:var(--red)}
.footer-info{position:absolute;left:95px;top:22px;color:var(--white);font-size:13px;line-height:21px}
.footer-info b{font-weight:700}
.footer-brand{position:absolute;left:482px;top:20px;width:162px;color:var(--white);font-family:"Libre Baskerville",serif;text-align:center;line-height:1}
.footer-brand .name{font-size:30px}
.footer-brand .sub{font-size:12px;letter-spacing:7px;margin-top:10px}
.badges{position:absolute;left:776px;top:18px;display:flex;gap:12px;align-items:flex-end}
.badges span{background:#e9e9e9;opacity:.9}
.footer-legal{position:absolute;right:100px;top:74px;text-align:right;color:var(--white);font-size:11px;line-height:21px}
</style>
</head>
<body>

<header>
  <div class="abs brand"><div class="name">Brannock</div><div class="sub">AUCTIONS</div></div>
  <div class="abs social">
    <span class="social-label">Social Media:</span>
    <span class="social-tile tile-a" role="img" aria-label="Social network link"></span>
    <span class="social-tile tile-b" role="img" aria-label="Microblog link"></span>
    <span class="social-tile tile-c" role="img" aria-label="News feed link"></span>
  </div>
</header>

<nav class="abs nav">
  <ul>
    <li>Home</li><li>Real Estate Listings</li><li class="active">Auctions</li><li>Buyers</li><li>Sellers</li><li>Services</li><li>Meet the Crew</li><li>Contact Us</li>
  </ul>
</nav>

<section class="abs slider" role="img" aria-label="Slideshow photo of a white stucco house with palm trees">
  <svg class="share" viewBox="0 0 26 26"><circle cx="13" cy="13" r="13" fill="#111"/><path d="M7 17c1-5 5-7 9-7V7l5 5-5 5v-3c-3 0-6 1-9 3z" fill="#fff"/></svg>
  <div class="dots"><span></span><span class="on"></span><span></span><span></span><span></span></div>
</section>
<div class="abs dropdown"><div>Upcoming auctions</div><div class="hover">Past auctions</div></div>

<aside class="abs alert">
  <h2>Auction Alert</h2>
  <p>Please join our free mailing list to get auction alerts for upcoming events.</p>
  <div class="field">Enter Your Email</div>
  <div class="btn">Sign Up</div>
</aside>

<p class="abs tagline">Brannock Auctions &amp; Realty, Inc. is the only call needed for all of your assets evaluation and disposition needs.</p>

<article class="abs listing">
  <div class="listing-head">612 HARBOR CREST DR</div>
  <div class="thumb" role="img" aria-label="Photo of the listed property"></div>
  <div class="action" style="top:174px"><svg width="20" height="18" viewBox="0 0 20 18"><rect x="1" y="3" width="12" height="12" rx="2" fill="#cfe3f5"/><path d="M4 7h6M4 10h6" stroke="#3a6ea5" stroke-width="1.5"/></svg>Details</div>
  <div class="action" style="top:217px"><svg width="20" height="18" viewBox="0 0 20 18"><rect x="1" y="2" width="17" height="14" fill="#f3d36b"/><rect x="3" y="5" width="13" height="9" fill="#5c9ad1"/></svg>Photos</div>
  <div class="listing-body">
    <h3>FT COMMERCIAL BUILDING</h3>
    <p class="desc">Selling 3120 Acres of land in tracts of 2590 Acres &amp; 560 Acres</p>
    <p class="sale-link">Click here to view Sale Bill!</p>
    <p class="strong">LIVE OFF-SITE AUCTION</p>
    <p style="font-weight:500">Auction Location:</p>
    <p><svg class="pin" width="9" height="13" viewBox="0 0 9 13"><path d="M4.5 0A4.5 4.5 0 0 1 9 4.5C9 8 4.5 13 4.5 13S0 8 0 4.5A4.5 4.5 0 0 1 4.5 0z" fill="#d6142d"/><circle cx="4.5" cy="4.5" r="1.6" fill="#fff"/></svg>418 N Elm Street, Fairhaven, OK 73950</p>
    <p style="font-weight:500">Property Location:</p>
    <p><svg class="pin" width="9" height="13" viewBox="0 0 9 13"><path d="M4.5 0A4.5 4.5 0 0 1 9 4.5C9 8 4.5 13 4.5 13S0 8 0 4.5A4.5 4.5 0 0 1 4.5 0z" fill="#d6142d"/><circle cx="4.5" cy="4.5" r="1.6" fill="#fff"/></svg>418 N Elm Street, Fairhaven, OK 73950</p>
    <p class="when">08/21/14 at 10:00 AM CDT</p>
  </div>
</article>

<div class="abs partner" role="img" aria-label="Platform partner badge"><span></span></div>

<section class="abs widget featured">
  <div class="widget-head">Featured Auctions</div>
  <p class="title">13.35 ACRES OF PRIME DEVELOP<br>&amp; 33RD STREET</p>
  <div class="img" role="img" aria-label="Photo of the featured auction property"></div>
  <p class="lots">LOTS 13 &amp; 14 FOR SALE, MILLBROOK<br>IOWA<br>Third Street, Millbrook, IA 52690</p>
</section>

<section class="abs widget testimonials">
  <div class="widget-head">Testimonials Blog</div>
  <blockquote><svg width="24" height="18" viewBox="0 0 30 22"><path d="M12 2C6 4 2 9 3 15a4 4 0 1 0 5-4c0-3 2-6 5-7zM27 2c-6 2-10 7-9 13a4 4 0 1 0 5-4c0-3 2-6 5-7z" fill="#aaa"/></svg>It is a long established fact that a reader will be distracted by the readable content of a page when looking at its layout. The point of using Lorem Ipsum is that it has a more-or-less normal distribution of letters...</blockquote>
  <p class="author">Dorian Vale...</p>
</section>

<footer class="abs footer">
  <div class="footer-info">
    <b>Brannock Auctions &amp; Realty, Inc.</b><br>
    30915 Quill Meadow Road • Suite 508 • Orlando, FL 32828<br>
    Office: 407.555.0142 / Cell: 407.555.0187 / Fax: 407.555.0163<br>
    Email: info@brannockauctions.example
  </div>
  <div class="footer-brand"><div class="name">Brannock</div><div class="sub">AUCTIONS</div></div>
  <div class="badges" role="img" aria-label="Professional affiliation badges">
    <span style="width:60px;height:40px;border-radius:4px"></span>
    <span style="width:36px;height:42px"></span>
    <span style="width:78px;height:30px"></span>
    <span style="width:32px;height:38px"></span>
  </div>
  <div class="footer-legal">Copyright © 2014 • Brannock Auctions, Inc. • All Rights Reserved<br>Powered by: BidWorks.example &amp; EMBERLINE</div>
</footer>

</body>
</html>
```